BUSINESS CARD - HALVERDINE RURAL SERVICES

I would like to create a business card for my fertilizer spreading business. I would like to incorporate my existing logo and also a description of the services offered. The business card will be given to farmers so must be kept simple but effective. It will also be left in stores so much also be eye catching in order to stand out from other cards.

Target Market(s)

FARMERS

Requirements
Must have
• FRONT OF CARD = EXISTING LOGO + "CUSTOMISED SPREADING" below the logo

REAR Of CARD = SERVICES OFFERED AND CONTACT DETAILS

- Bulk fertilizer including Lime, Gypsum, Manure & Compost
- Granular fertilizer including Single Super, Urea, Gran-am, & Custom Blends
- Modern equipment - Autosteer & Variable Rate Capable
- Friendly & Reliable Service
- Contact Gus: 0471 502 318
Nice to have
• utilize same color scheme as existing logo

```html
<!DOCTYPE html>
<html lang="en">
<head>
<meta charset="utf-8">
<title>Halverdine Rural Services – Business Card</title>
<link href="https://fonts.googleapis.com/css2?family=Source+Sans+3:ital,wght@0,700;1,700&display=swap" rel="stylesheet">
<style>
  :root {
    --backdrop: #e7d2ad;
    --card: #ffffff;
    --orange: #f0962e;
    --charcoal: #58585a;
    --faint: #ededed;
  }
  html, body {
    margin: 0;
    padding: 0;
    width: 1200px;
    height: 1100px;
    overflow: hidden;
    background: var(--backdrop);
    font-family: "Source Sans 3", "Source Sans Pro", Arial, sans-serif;
  }
  .canvas {
    position: relative;
    width: 1200px;
    height: 1100px;
  }
  .card {
    position: absolute;
    left: 272px;
    width: 677px;
    height: 387px;
    background: var(--card);
    overflow: hidden;
  }
  .card--front { top: 93px; }
  .card--back { top: 600px; }

  /* Front */
  .brand {
    position: absolute;
    left: 0;
    right: 0;
    top: 48px;
    display: flex;
    flex-direction: column;
    align-items: center;
  }
  .brand__mark {
    width: 150px;
    height: 150px;
    border-radius: 50%;
    background: var(--charcoal);
  }
  .brand__name {
    margin-top: 26px;
    font-weight: 700;
    font-size: 42px;
    line-height: 1;
    letter-spacing: -0.5px;
    color: var(--charcoal);
    white-space: nowrap;
  }
  .tagline-band {
    position: absolute;
    left: 0;
    bottom: 0;
    width: 677px;
    height: 47px;
  }
  .tagline {
    position: absolute;
    bottom: 0;
    height: 47px;
    display: flex;
    align-items: center;
    font-style: italic;
    font-weight: 700;
    font-size: 30px;
    letter-spacing: 6px;
    color: #ffffff;
  }
  .tagline--left { left: 80px; }
  .tagline--right { left: 358px; }

  /* Back */
  .corner-accent {
    position: absolute;
    left: 0;
    bottom: 0;
    width: 180px;
    height: 160px;
  }
  .faint-mark {
    position: absolute;
    left: 443px;
    top: 112px;
    width: 180px;
    height: 180px;
    border-radius: 50%;
    background: var(--faint);
  }
  .services {
    position: absolute;
    left: 0;
    right: 0;
    top: 40px;
    text-align: center;
    font-style: italic;
    font-weight: 700;
    font-size: 22px;
    line-height: 29px;
  }
  .service { margin: 0 0 27px; }
  .service__title { color: var(--orange); display: block; }
  .service__detail { color: var(--charcoal); display: block; }
</style>
</head>
<body>
<div class="canvas">

  <section class="card card--front">
    <div class="brand">
      <div class="brand__mark"></div>
      <div class="brand__name">Halverdine Rural Services</div>
    </div>
    <svg class="tagline-band" viewBox="0 0 677 47" aria-hidden="true">
      <polygon points="0,0 325,0 348,47 0,47" fill="var(--orange)"/>
      <polygon points="333,0 677,0 677,47 356,47" fill="var(--charcoal)"/>
    </svg>
    <div class="tagline tagline--left">CUSTOMISED</div>
    <div class="tagline tagline--right">SPREADING</div>
  </section>

  <section class="card card--back">
    <div class="faint-mark"></div>
    <svg class="corner-accent" viewBox="0 0 180 160" aria-hidden="true">
      <polygon points="18,0 173,160 146,160 18,28" fill="var(--charcoal)"/>
      <polygon points="0,8 146,160 0,160" fill="var(--orange)"/>
    </svg>
    <div class="services">
      <p class="service">
        <span class="service__title">Bulk Fertilizer</span>
        <span class="service__detail">lime, gypsum, manure &amp; compost</span>
      </p>
      <p class="service">
        <span class="service__title">Granular Fertilizer</span>
        <span class="service__detail">single super, urea, gram-am &amp; custom blends</span>
      </p>
      <p class="service">
        <span class="service__title">Modern equipment</span>
        <span class="service__detail">Auto steer &amp; variable rate capability</span>
      </p>
      <p class="service">
        <span class="service__title">Gus</span>
        <span class="service__detail">0471 502 318</span>
      </p>
    </div>
  </section>

</div>
</body>
</html>
```